Aviation Banner Ad Designs

SkyLedgerMetrics provides access to the most accurate aircraft operating cost information, to compare Piston, Turboprop and Jet aircraft.

The banners ads will be used for retargeting/remarketing - to bring visitors back to the site. The banners should remind and reinforce the key messages of what the site provides.

Target Market(s)

Private aircraft buyers including:
- Aircraft Brokers
- Charter Operators
- Corporate Flight Departments
- Aircraft Management companies
- Financial Institutions
- Aircraft Owners
- Prospective Buyers

Requirements
Must have
• A. Banner Objective
The visual and textual content of the banner should remind the viewer about the features of the site, and prompt them to return to the site.
1. Arresting visual
2. Headline
3. Single message
4. Compelling CTA
5. Logo - big enough to see
6. Standard DWR ad sizes/specs

B. Design Elements
Logo: As attached
Main Title: Calculate Jet Operating Costs
Subtitle: Compare Ownership Usage Scenarios
Call to Action Button: Compare Ownership Costs
Background: Several images supplied as options

C. Banner Sizes
Do examples as 300×250 , 728×90 , 160×600
Final sizes to also include 320×100 , 336x280 , 300x600

Finally delivery as .jpg files.

Font - use same font as on site

```html
<!DOCTYPE html>
<html lang="en">
<head>
<meta charset="utf-8">
<title>SkyLedgerMetrics Banner Set</title>
<link href="https://fonts.googleapis.com/css2?family=Oswald:wght@600&family=Roboto:wght@400;500&display=swap" rel="stylesheet">
<style>
  :root {
    --page-bg: #262626;
    --navy: #001a4e;
    --teal: #17a2b8;
    --white: #ffffff;
    --ink: #1a1a1a;
    --rule: #0a0f1e;
    --sky-top: #3f6fb5;
    --sky-mid: #8fb2de;
    --metal: #d9dde3;
  }
  * { box-sizing: border-box; margin: 0; padding: 0; }
  html, body { width: 1200px; height: 960px; overflow: hidden; background: var(--page-bg); }
  .stage { position: absolute; left: 0; top: 0; width: 1000px; height: 800px; transform: scale(1.2); transform-origin: 0 0; }
  .banner { position: absolute; overflow: hidden; background: var(--navy); font-family: "Roboto", Arial, sans-serif; color: var(--white); }
  .banner svg.shapes { position: absolute; left: 0; top: 0; }
  .brand { position: absolute; display: flex; align-items: center; gap: 7px; font-family: "Roboto", Arial, sans-serif; font-weight: 500; color: var(--ink); letter-spacing: 0.2px; white-space: nowrap; }
  .brand-mark { width: 14px; height: 14px; background: var(--teal); flex: none; }
  .headline { position: absolute; font-family: "Oswald", "Arial Narrow", sans-serif; font-weight: 600; text-align: center; line-height: 1.08; letter-spacing: -0.3px; white-space: nowrap; }
  .subline { position: absolute; text-align: center; font-weight: 400; line-height: 1.2; white-space: nowrap; }
  .rule { position: absolute; height: 1px; background: var(--rule); }
  .cta { position: absolute; display: flex; align-items: center; justify-content: center; background: var(--teal); color: var(--white); border-radius: 3px; font-weight: 500; white-space: nowrap; box-shadow: 0 2px 3px rgba(0,0,0,0.3); }

  /* 728 x 90 */
  .leaderboard { left: 20px; top: 15px; width: 728px; height: 90px; }
  .leaderboard .brand { left: 14px; top: 36px; font-size: 14px; }
  .leaderboard .headline { left: 400px; top: 7px; width: 150px; font-size: 17px; letter-spacing: -0.4px; }
  .leaderboard .subline { left: 400px; top: 54px; width: 150px; font-size: 10.5px; }
  .leaderboard .divider { position: absolute; left: 549px; top: 12px; width: 1px; height: 64px; background: var(--rule); }
  .leaderboard .cta { left: 571px; top: 26px; width: 141px; height: 33px; font-size: 11px; }

  /* 160 x 600 */
  .skyscraper { left: 20px; top: 125px; width: 160px; height: 600px; }
  .skyscraper .brand { left: 10px; top: 22px; font-size: 12.5px; gap: 5px; }
  .skyscraper .brand-mark { width: 12px; height: 12px; }
  .skyscraper .headline { left: 0; top: 382px; width: 160px; font-size: 22px; }
  .skyscraper .rule { left: 18px; top: 448px; width: 124px; }
  .skyscraper .subline { left: 0; top: 463px; width: 160px; font-size: 16px; }
  .skyscraper .cta { left: 9px; top: 542px; width: 141px; height: 33px; font-size: 11px; }

  /* 300 x 250 */
  .rectangle { left: 200px; top: 125px; width: 300px; height: 250px; }
  .rectangle .brand { left: 12px; top: 24px; font-size: 12.5px; gap: 5px; }
  .rectangle .brand-mark { width: 12px; height: 12px; }
  .rectangle .headline { left: 0; top: 75px; width: 160px; font-size: 20px; }
  .rectangle .rule { left: 35px; top: 131px; width: 90px; }
  .rectangle .subline { left: 0; top: 142px; width: 160px; font-size: 14px; }
  .rectangle .cta { left: 13px; top: 195px; width: 171px; height: 40px; font-size: 12px; }
</style>
</head>
<body>
<div class="stage">

  <section class="banner leaderboard" aria-label="728 by 90 banner">
    <svg class="shapes" width="728" height="90" viewBox="0 0 728 90">
      <defs>
        <linearGradient id="lb-photo" x1="0" y1="0" x2="1" y2="1">
          <stop offset="0" stop-color="#3f6fb5"/>
          <stop offset="0.55" stop-color="#d9dde3"/>
          <stop offset="1" stop-color="#8fb2de"/>
        </linearGradient>
      </defs>
      <rect width="728" height="90" fill="#001a4e"/>
      <rect width="200" height="90" fill="#ffffff"/>
      <path d="M176,0 Q158,45 176,90 L392,90 Q410,45 392,0 Z" fill="#17a2b8"/>
      <path d="M182,0 Q164,45 182,90 L386,90 Q404,45 386,0 Z" fill="url(#lb-photo)" role="img" aria-label="Photo of a business jet engine and fuselage against blue sky"/>
    </svg>
    <div class="brand"><span class="brand-mark"></span>SkyLedgerMetrics</div>
    <h2 class="headline">Calculate Jet<br>Operating Costs</h2>
    <p class="subline">Compare Ownership<br>Usage Scenarios</p>
    <span class="divider"></span>
    <a class="cta">Compare Ownership Costs</a>
  </section>

  <section class="banner skyscraper" aria-label="160 by 600 banner">
    <svg class="shapes" width="160" height="600" viewBox="0 0 160 600">
      <defs>
        <linearGradient id="sk-photo" x1="0" y1="0" x2="0.6" y2="1">
          <stop offset="0" stop-color="#3f6fb5"/>
          <stop offset="0.5" stop-color="#d9dde3"/>
          <stop offset="1" stop-color="#8fb2de"/>
        </linearGradient>
      </defs>
      <rect width="160" height="600" fill="#001a4e"/>
      <rect width="160" height="80" fill="#ffffff"/>
      <path d="M0,70 Q80,54 160,70 L160,360 Q80,378 0,360 Z" fill="#17a2b8"/>
      <path d="M0,76 Q80,61 160,76 L160,354 Q80,370 0,354 Z" fill="url(#sk-photo)" role="img" aria-label="Photo of a business jet engine close-up against cloudy blue sky"/>
    </svg>
    <div class="brand"><span class="brand-mark"></span>SkyLedgerMetrics</div>
    <h2 class="headline">Calculate Jet<br>Operating Costs</h2>
    <span class="rule"></span>
    <p class="subline">Compare<br>Ownership Usage<br>Scenarios</p>
    <a class="cta">Compare Ownership Costs</a>
  </section>

  <section class="banner rectangle" aria-label="300 by 250 banner">
    <svg class="shapes" width="300" height="250" viewBox="0 0 300 250">
      <defs>
        <linearGradient id="mr-photo" x1="0" y1="0" x2="0.8" y2="1">
          <stop offset="0" stop-color="#3f6fb5"/>
          <stop offset="0.5" stop-color="#d9dde3"/>
          <stop offset="1" stop-color="#8fb2de"/>
        </linearGradient>
      </defs>
      <rect width="300" height="250" fill="#001a4e"/>
      <rect width="180" height="63" fill="#ffffff"/>
      <path d="M176,0 Q148,125 160,250 L300,250 L300,0 Z" fill="#17a2b8"/>
      <path d="M182,0 Q154,125 166,250 L300,250 L300,0 Z" fill="url(#mr-photo)" role="img" aria-label="Photo of a business jet engine and wing against blue sky"/>
    </svg>
    <div class="brand"><span class="brand-mark"></span>SkyLedgerMetrics</div>
    <h2 class="headline">Calculate Jet<br>Operating Costs</h2>
    <span class="rule"></span>
    <p class="subline">Compare Ownership<br>Usage Scenarios</p>
    <a class="cta">Compare Ownership Costs</a>
  </section>

</div>
</body>
</html>
```